Business card required for IT Consultancy Business - Bluefern Consulting.
Company provides the whole nine yards of services across IT Architecture, design and execution.
Basically we provide consulting services to help businesses make sure their technology is enabling their business strategy.
Design for front and back required.
We would like the front of the card to inlcude:
Name
Title
Mobile number
email address
www.BFQ.com.au
Company logos attached.
Thank you
Industry/Entity Type
Business
Contact Information for Business Card
Name
Title
Mobile number
email address
www.BFQ.com.au
Look and feel
Each slider illustrates characteristics of the customer's brand and the style your logo design should communicate.

```html
<!DOCTYPE html>
<html lang="en">
<head>
<meta charset="utf-8">
<title>Bluefern Consulting – Business Card</title>
<link href="https://fonts.googleapis.com/css2?family=Oswald:wght@600&family=Jost:wght@400;500&display=swap" rel="stylesheet">
<style>
  :root {
    --stage: #2b2b2b;
    --card: #1d1d1e;
    --card-edge: #262627;
    --ink: #f2f2f2;
    --silver: #b9babc;
    --accent: #2f80c8;
    --rule: #cfcfcf;
  }
  * { margin: 0; padding: 0; box-sizing: border-box; }
  html, body { width: 1200px; height: 1000px; overflow: hidden; }
  body {
    background: var(--stage);
    font-family: "Jost", "Futura", sans-serif;
    color: var(--ink);
    position: relative;
  }
  .card {
    position: absolute;
    left: 280px;
    width: 640px;
    height: 366px;
    background: var(--card);
    border: 1px solid var(--card-edge);
    box-shadow: 0 18px 40px rgba(0,0,0,.45);
  }
  .card--back { top: 90px; }
  .card--front { top: 530px; }

  /* back */
  .brand-name {
    position: absolute;
    top: 150px;
    left: 0; right: 0;
    text-align: center;
    font-weight: 500;
    font-size: 42px;
    letter-spacing: 1px;
    color: var(--silver);
  }
  .back-url {
    position: absolute;
    bottom: 34px;
    left: 0; right: 0;
    text-align: center;
    font-size: 15px;
    letter-spacing: 2px;
  }
  .accent { color: var(--accent); }

  /* front */
  .identity {
    position: absolute;
    top: 140px;
    right: 370px;
    text-align: right;
  }
  .identity__name {
    font-family: "Oswald", "Impact", sans-serif;
    font-weight: 600;
    font-size: 38px;
    letter-spacing: 2px;
    line-height: 1.05;
    text-transform: uppercase;
  }
  .identity__title {
    font-size: 21px;
    letter-spacing: 1px;
    color: var(--accent);
    line-height: 1.1;
  }
  .divider {
    position: absolute;
    left: 285px;
    top: 138px;
    width: 1px;
    height: 88px;
    background: var(--rule);
  }
  .contacts {
    position: absolute;
    left: 305px;
    top: 140px;
    list-style: none;
  }
  .contacts li {
    display: flex;
    align-items: center;
    gap: 12px;
    font-size: 18px;
    letter-spacing: 1.5px;
    line-height: 28px;
  }
  .contacts svg, .address svg { width: 14px; height: 14px; fill: var(--accent); flex: none; }
  .address {
    position: absolute;
    left: 200px;
    top: 288px;
    display: flex;
    align-items: center;
    gap: 10px;
    font-size: 18px;
    letter-spacing: 1.5px;
  }
  .corner-mark {
    position: absolute;
    right: 22px;
    bottom: 20px;
    font-weight: 500;
    font-size: 16px;
    color: var(--accent);
    letter-spacing: 1px;
  }
</style>
</head>
<body>

<section class="card card--back">
  <p class="brand-name">Bluefern Consulting</p>
  <p class="back-url">www.<span class="accent">BFQ</span>.com.au</p>
</section>

<section class="card card--front">
  <div class="identity">
    <p class="identity__name">Daniel Hart</p>
    <p class="identity__title">Founder/CEO</p>
  </div>
  <div class="divider"></div>
  <ul class="contacts">
    <li>
      <svg viewBox="0 0 24 24" aria-hidden="true"><path d="M6.6 10.8a15.1 15.1 0 0 0 6.6 6.6l2.2-2.2a1 1 0 0 1 1-.25 11.4 11.4 0 0 0 3.6.57 1 1 0 0 1 1 1V20a1 1 0 0 1-1 1A17 17 0 0 1 3 4a1 1 0 0 1 1-1h3.5a1 1 0 0 1 1 1c0 1.25.2 2.45.57 3.6a1 1 0 0 1-.25 1z"/></svg>
      (000) 555-0182
    </li>
    <li>
      <svg viewBox="0 0 24 24" aria-hidden="true"><path d="M2 5h20v2l-10 6L2 7z M2 9l10 6 10-6v10H2z"/></svg>
      daniel@bfqmail.com
    </li>
    <li>
      <svg viewBox="0 0 24 24" aria-hidden="true"><path d="M12 2a10 10 0 1 0 0 20 10 10 0 0 0 0-20zm6.9 6h-3a15.6 15.6 0 0 0-1.4-3.6A8 8 0 0 1 18.9 8zM12 4c.8 1.2 1.5 2.5 1.9 4h-3.8c.4-1.5 1.1-2.8 1.9-4zM4.3 14a8.2 8.2 0 0 1 0-4h3.4a16.5 16.5 0 0 0 0 4zm.8 2h3a15.6 15.6 0 0 0 1.4 3.6A8 8 0 0 1 5.1 16zm3-8h-3a8 8 0 0 1 4.4-3.6C8.9 5.5 8.4 6.7 8.1 8zM12 20c-.8-1.2-1.5-2.5-1.9-4h3.8c-.4 1.5-1.1 2.8-1.9 4zm2.3-6H9.7a14.7 14.7 0 0 1 0-4h4.6a14.7 14.7 0 0 1 0 4zm.2 5.6c.6-1.1 1.1-2.3 1.4-3.6h3a8 8 0 0 1-4.4 3.6zm1.8-5.6a16.5 16.5 0 0 0 0-4h3.4a8.2 8.2 0 0 1 0 4z"/></svg>
      www.<span class="accent">bfq</span>.com.au
    </li>
  </ul>
  <p class="address">
    <svg viewBox="0 0 24 24" aria-hidden="true"><path d="M12 2a7 7 0 0 0-7 7c0 5.2 7 13 7 13s7-7.8 7-13a7 7 0 0 0-7-7zm0 9.5A2.5 2.5 0 1 1 12 6.5a2.5 2.5 0 0 1 0 5z"/></svg>
    Your Street Address, NewYork, 1234
  </p>
  <p class="corner-mark">BFQ</p>
</section>

</body>
</html>
```